We are a Leadership Specialist Boutique Business that is launching a residential womans workshop....

We need a post card which will include our logo, an overview of our workshop, a catch statement on one side and on the other side dates, venue, facilitators and contacts to book the workshop. The postcards will be distributed at an Riverbend Harvest Gala Lunch. They will be placed at each setting of the lunch attendees. The company QVR running the lunch is a sponsor of our business.

Target Market(s)

Women supervisor to middle management positions or own business

Industry/Entity Type

Academic Training

Font styles to use
Serif

Colors
34a7d8

Requirements
Must have
• Use Colour Palette on docs attached, Logo, Workshop overview either the Circle Theory or the Core Philosophy Text,
• The dates, venue, all costs of the program including discount code. One catch sentence that grabs the audience from the content I have provided that appeals to the designer
• Must have these contacts.
• Website: brightpathcircle.com,au
• Email: Info@brightpathcircle.com.au.
• Phone: 0491735206
Nice to have
• Facilitators Photos and names

```html
<!DOCTYPE html>
<html lang="en">
<head>
<meta charset="utf-8">
<title>Bright Path Circle – Postcard</title>
<link href="https://fonts.googleapis.com/css2?family=Raleway:wght@400;500;700;800;900&display=swap" rel="stylesheet">
<style>
  :root {
    --backdrop: #e8e8e8;
    --mint: #c4e5de;
    --paper: #ffffff;
    --navy: #1c1f45;
    --ink: #2a2a2a;
    --photo-tone: #9a9a9a;
    --rule: #6d6d6d;
  }
  * { box-sizing: border-box; margin: 0; padding: 0; }
  html, body { width: 1200px; height: 959px; overflow: hidden; }
  body {
    background: var(--backdrop);
    font-family: "Raleway", sans-serif;
    position: relative;
  }
  .postcard {
    position: absolute;
    width: 690px;
    height: 450px;
    overflow: hidden;
    box-shadow: 0 6px 18px rgba(0,0,0,.18);
  }
  /* FRONT */
  .postcard--front { left: 90px; top: 16px; background: var(--mint); }
  .brand-disc {
    position: absolute; left: -50px; top: -60px;
    width: 400px; height: 400px; border-radius: 50%;
    background: var(--paper);
  }
  .brand-ring { position: absolute; left: 30px; top: 40px; }
  .brand-name {
    position: absolute; left: 55px; top: 126px; width: 190px;
    text-align: center; color: var(--ink);
    font-size: 30px; font-weight: 800; line-height: 1.12;
  }
  .philosophy {
    position: absolute; left: 320px; top: 42px; width: 350px;
    text-align: center; color: var(--navy);
  }
  .philosophy__title { font-size: 26px; font-weight: 900; line-height: 1.15; margin-bottom: 14px; }
  .philosophy__term { font-size: 17px; font-weight: 900; margin-top: 8px; }
  .philosophy__text { font-size: 15px; font-weight: 500; color: var(--ink); line-height: 1.2; }
  .catch-line {
    position: absolute; left: 60px; right: 20px; top: 322px;
    text-align: center; color: var(--navy);
    font-size: 14px; font-weight: 800;
  }
  .contact-band {
    position: absolute; left: 0; right: 0; bottom: 0; height: 104px;
    background: var(--paper);
  }
  .contact-band__links {
    position: absolute; left: 60px; top: 20px;
    font-size: 14px; font-weight: 700; color: var(--ink); line-height: 1.5;
  }
  .contact-band__phone {
    position: absolute; left: 330px; top: 34px;
    font-size: 42px; font-weight: 800; color: var(--ink); letter-spacing: 1px;
  }
  /* BACK */
  .postcard--back { left: 420px; top: 492px; background: var(--paper); }
  .back-panel {
    position: absolute; left: 0; top: 0; width: 350px; height: 100%;
    background: var(--mint);
  }
  .facilitator {
    position: absolute; width: 150px; text-align: center; color: var(--ink);
  }
  .facilitator--one { left: 20px; top: 36px; }
  .facilitator--two { left: 175px; top: 14px; }
  .facilitator__photo {
    width: 82px; height: 82px; border-radius: 50%; margin: 0 auto 6px;
    background: radial-gradient(circle at 50% 40%, #c9c9c9, var(--photo-tone));
    border: 2px solid #8a8a8a;
  }
  .facilitator__name { font-size: 14px; font-weight: 800; }
  .facilitator__role { font-size: 11px; font-weight: 700; line-height: 1.15; }
  .program-box {
    position: absolute; left: 18px; top: 170px; width: 315px; height: 190px;
    text-align: center; color: var(--ink); padding: 10px 14px;
  }
  .program-box__frame { position: absolute; left: 0; top: 0; }
  .program-box h3 { font-size: 15px; font-weight: 900; margin-top: 2px; }
  .program-box p { font-size: 10px; font-weight: 500; line-height: 1.3; }
  .program-box .price { font-size: 10px; font-weight: 800; margin-top: 5px; }
  .back-phone {
    position: absolute; left: 22px; bottom: 20px;
    font-size: 38px; font-weight: 800; color: var(--ink); letter-spacing: 1px;
  }
  .address-line {
    position: absolute; left: 385px; width: 270px; height: 0;
    border-top: 1.5px solid var(--rule);
  }
</style>
</head>
<body>

<section class="postcard postcard--front">
  <div class="brand-disc"></div>
  <svg class="brand-ring" width="240" height="240" viewBox="0 0 240 240" aria-hidden="true">
    <circle cx="120" cy="120" r="112" fill="none" stroke="#2a2a2a" stroke-width="9"/>
  </svg>
  <div class="brand-name">Bright Path<br>Circle</div>

  <div class="philosophy">
    <h2 class="philosophy__title">THE CORE PHILOSOPHY<br>OF THE PROGRAMZ</h2>
    <h4 class="philosophy__term">WORLDVIEW</h4>
    <p class="philosophy__text">A view Held inside of us as to ho<br>things work.</p>
    <h4 class="philosophy__term">BIASES</h4>
    <p class="philosophy__text">Our own behaviours and the<br>behaviours of others that reinforce<br>this worldviews.</p>
    <h4 class="philosophy__term">ERROR SCRIPTS</h4>
    <p class="philosophy__text">Stories implanted by us or others that<br>limits our potential.</p>
  </div>

  <p class="catch-line">Rewiting a new Personal Narrative allows us to shatter our own glass celing</p>

  <div class="contact-band">
    <div class="contact-band__links">
      brightpathcircle.com,au<br>
      Info@brightpathcircle.com.au
    </div>
    <div class="contact-band__phone">0491735206</div>
  </div>
</section>

<section class="postcard postcard--back">
  <div class="back-panel">
    <div class="facilitator facilitator--one">
      <div class="facilitator__photo" role="img" aria-label="Portrait photo of facilitator Dana Whitcombe"></div>
      <div class="facilitator__name">Dana Whitcombe</div>
      <div class="facilitator__role">An intutive advisor to<br>empowered women</div>
    </div>
    <div class="facilitator facilitator--two">
      <div class="facilitator__photo" role="img" aria-label="Portrait photo of facilitator Colin Ashgrove"></div>
      <div class="facilitator__name">Colin Ashgrove</div>
      <div class="facilitator__role">Trusted Advisor to<br>wise women</div>
    </div>

    <div class="program-box">
      <svg class="program-box__frame" width="315" height="190" viewBox="0 0 315 190" aria-hidden="true">
        <path d="M40 2 H313 V60 M275 188 H2 V130" fill="none" stroke="#2a2a2a" stroke-width="3"/>
      </svg>
      <h3>Program and Upcoming Dates</h3>
      <p>2 ½ Days residential – 26th to 28th May 2019<br>
      May Venue – The Larchmont Lodge, Ashford NSW<br>
      Future Programs – August, October, March</p>
      <h3>Why</h3>
      <p>The program is emersive and wholistic which includes development of your life and leadership skills, by rewriting your narrative and a personal action plan for change</p>
      <p class="price">$3,495 (Early Bird Book by 26th April) $3,095<br>Quote QVR Code 9455 for a further $100 Discount</p>
    </div>

    <div class="back-phone">0491735206</div>
  </div>

  <div class="address-line" style="top:250px"></div>
  <div class="address-line" style="top:305px"></div>
  <div class="address-line" style="top:360px"></div>
</section>

</body>
</html>
```